I need a business card for my original fine art pieces

I would like a business card design including a logo design for a new business in the art world. I am based in the Hunter Valley NSW Australia. I am a contemporary figurative, encaustic and wildlife artist. I would like to be able to upload my email and mobile number to this as well. This design should be one that I can incorporate into banners and flyers etc. Id like to incorporate one of my own images or partial image into the background or somewhere below. My initials are KR and I would like these used as a logo type. I would like the use of some colour and it to be bright and catchy. The final design should communicate artwork custom made and commissions available.

Overview: Original Fine Artworks for sale, online, art galleries etc, Custom made to order and by commission.

Target market is world wide audience and corporate world

My figurative work is painted using acrylics in a lot of natural ochre colours that reflect the Australian Outback, on canvas, linen, paper or board: My encaustic work is created in a contemporary abstract style using a blow torch and a made with a medium of 100% pure bees wax, Damar resin, mixed media and coloured pigments, applied to Birch board. My wildlife are created using coloured pencil and mixed media on a variety of paper types or board.

```html
<!DOCTYPE html>
<html lang="en">
<head>
<meta charset="utf-8">
<title>Kira Rennick Fine Artworks – Business Card</title>
<link rel="stylesheet" href="https://fonts.googleapis.com/css2?family=Jost:wght@400&display=swap">
<style>
  :root {
    --page-bg: #ffffff;
    --card-black: #000000;
    --accent-orange: #ec4a23;
    --accent-orange-soft: #f3672f;
    --ink-black: #111111;
    --paper-white: #ffffff;
    --card-shadow: rgba(0, 0, 0, 0.35);
  }
  * { margin: 0; padding: 0; box-sizing: border-box; }
  html, body {
    width: 1200px;
    height: 1200px;
    overflow: hidden;
    background: var(--page-bg);
  }
  .canvas {
    position: relative;
    width: 1200px;
    height: 1200px;
  }
  .card {
    position: absolute;
    top: 444px;
    height: 305px;
    display: flex;
    overflow: hidden;
    box-shadow: 2px 3px 5px var(--card-shadow);
    font-family: "Jost", "Futura", sans-serif;
  }
  .card--front { left: 27px; width: 530px; }
  .card--back { left: 635px; width: 533px; }

  /* Front */
  .front-brand {
    width: 349px;
    height: 100%;
    background: var(--card-black);
    position: relative;
    text-align: center;
  }
  .monogram {
    position: absolute;
    top: 34px;
    left: 0;
    width: 100%;
    font-size: 96px;
    line-height: 1;
    font-weight: 400;
    color: var(--accent-orange);
    letter-spacing: 2px;
  }
  .artist-name {
    position: absolute;
    top: 188px;
    left: 0;
    width: 100%;
    font-size: 29px;
    font-weight: 400;
    letter-spacing: 2px;
    color: var(--accent-orange);
    line-height: 1;
  }
  .artist-tagline {
    position: absolute;
    top: 226px;
    left: 0;
    width: 100%;
    font-size: 16px;
    font-weight: 400;
    letter-spacing: 2.5px;
    color: var(--paper-white);
    line-height: 1;
  }
  .artwork {
    height: 100%;
  }
  .artwork--seated-figure {
    width: 181px;
    background:
      radial-gradient(ellipse 55% 45% at 55% 65%, #e0b27a 0%, #b97a4e 45%, transparent 75%),
      radial-gradient(ellipse 40% 30% at 50% 22%, #a8583a 0%, transparent 70%),
      linear-gradient(160deg, #2a2522 0%, #3a2f28 50%, #1c1a19 100%);
  }

  /* Back */
  .artwork--torso {
    width: 237px;
    background:
      radial-gradient(ellipse 30% 70% at 48% 50%, #e8c46a 0%, #b59a62 35%, transparent 70%),
      radial-gradient(ellipse 25% 40% at 80% 85%, #d9a86a 0%, transparent 70%),
      linear-gradient(100deg, #5b5a5e 0%, #3a3840 40%, #141214 70%, #262226 100%);
  }
  .back-contact {
    flex: 1;
    height: 100%;
    background: var(--accent-orange);
    position: relative;
    text-align: center;
  }
  .monogram-watermark {
    position: absolute;
    top: 18px;
    left: 0;
    width: 100%;
    font-size: 230px;
    line-height: 1;
    font-weight: 400;
    color: var(--accent-orange-soft);
  }
  .contact-list {
    position: absolute;
    top: 115px;
    left: 0;
    width: 100%;
    list-style: none;
    font-size: 17px;
    line-height: 20.5px;
    letter-spacing: 2.2px;
    color: var(--ink-black);
  }
</style>
</head>
<body>
<main class="canvas">
  <section class="card card--front" aria-label="Business card front">
    <div class="front-brand">
      <div class="monogram">KR</div>
      <h1 class="artist-name">KIRA RENNICK</h1>
      <p class="artist-tagline">FINE ARTWORKS</p>
    </div>
    <div class="artwork artwork--seated-figure" role="img" aria-label="Painting of a seated nude figure hugging its knees, warm ochre tones on a dark ground"></div>
  </section>

  <section class="card card--back" aria-label="Business card back">
    <div class="artwork artwork--torso" role="img" aria-label="Painting detail of a curved figure torso in yellow and grey light against a black ground"></div>
    <div class="back-contact">
      <div class="monogram-watermark" aria-hidden="true">KR</div>
      <ul class="contact-list">
        <li>88 VINE LANE</li>
        <li>POKOLBIN NSW</li>
        <li>0400 555 182</li>
        <li>WWW.KIRARENNICK.ART</li>
      </ul>
    </div>
  </section>
</main>
</body>
</html>
```